digger and truck hire

this is a new business - Digger and Truck
we would like to include the attached photo of the digger and truck - as the truck is red and the digger is green
maybe either black or white lettering which ever suits

Industry/Entity Type

Business

Contact Information for Business Card

RDL - Ruddas 2.5t Mini Digger and 7t Tip Truck -Hire, full attachments, augers, trenching, site preparation, small aggregate deliveries
Phone 0218365914
rudda.rdl@plinto.co.nz

```html
<!DOCTYPE html>
<html lang="en">
<head>
<meta charset="utf-8">
<title>RDL - Ruddas Business Card</title>
<link rel="stylesheet" href="https://fonts.googleapis.com/css2?family=Arvo:wght@700&display=swap">
<style>
  :root {
    --ink-white: #ffffff;
    --ink-shadow: #1a1a1a;
    --digger-green: #23a03c;
    --truck-red: #e01b22;
    --band-black: #0b0b0b;
    --scene-sky: #c9ccd0;
    --scene-shed: #9a9ea3;
    --scene-red: #b8282c;
    --scene-teal: #3fa58e;
    --scene-ground: #5e5a55;
  }
  html, body {
    margin: 0;
    padding: 0;
    overflow: hidden;
    background: #ffffff;
  }
  .card {
    position: relative;
    width: 1200px;
    height: 740px;
    overflow: hidden;
    font-family: "Arvo", "Rockwell", serif;
    color: var(--ink-white);
  }
  .card__photo {
    position: absolute;
    inset: 0;
    background:
      linear-gradient(180deg, rgba(201,204,208,0.9) 0%, rgba(154,158,163,0.75) 30%, rgba(0,0,0,0) 55%),
      linear-gradient(90deg, var(--scene-red) 0%, #c8474a 30%, #8f7b74 52%, var(--scene-teal) 72%, #8c9196 100%);
  }
  .card__photo::after {
    content: "";
    position: absolute;
    inset: 0;
    background: linear-gradient(180deg, rgba(0,0,0,0) 60%, var(--scene-ground) 100%);
    opacity: 0.6;
  }
  .text-shadowed {
    text-shadow: 3px 3px 0 var(--ink-shadow), 4px 4px 3px rgba(0,0,0,0.6);
  }
  .card__title {
    position: absolute;
    left: 66px;
    top: 58px;
    margin: 0;
    font-size: 80px;
    line-height: 1;
    font-weight: 700;
    letter-spacing: 1px;
  }
  .card__title-rule {
    position: absolute;
    left: 66px;
    top: 146px;
    width: 762px;
    height: 3px;
    background: var(--ink-white);
    box-shadow: 2px 2px 0 var(--ink-shadow);
  }
  .card__tagline {
    position: absolute;
    left: 66px;
    top: 172px;
    margin: 0;
    font-size: 41px;
    line-height: 1;
    font-weight: 700;
  }
  .tagline__digger { color: var(--digger-green); }
  .tagline__truck { color: var(--truck-red); }
  .services {
    position: absolute;
    margin: 0;
    padding: 0;
    list-style: none;
    font-size: 41px;
    line-height: 65px;
    font-weight: 700;
  }
  .services--left { left: 70px; top: 264px; }
  .services--right { left: 672px; top: 291px; }
  .services li::before {
    content: "\2022";
    display: inline-block;
    width: 26px;
    font-size: 30px;
    vertical-align: 4px;
  }
  .services .services__wrap::before { content: ""; }
  .card__band {
    position: absolute;
    left: 0;
    bottom: 0;
    width: 1200px;
    height: 140px;
    background: var(--band-black);
  }
  .contact {
    position: absolute;
    top: 630px;
    margin: 0;
    font-size: 32px;
    line-height: 1;
    font-weight: 700;
    letter-spacing: 0.5px;
  }
  .contact--phone { left: 84px; }
  .contact--email { left: 611px; }
</style>
</head>
<body>
  <main class="card">
    <div class="card__photo" role="img" aria-label="Photo of a red tip truck carrying a green mini digger strapped down on its tray, in front of a grey shed"></div>

    <h1 class="card__title text-shadowed">RDL - Ruddas</h1>
    <div class="card__title-rule"></div>

    <p class="card__tagline text-shadowed">
      <span class="tagline__digger">2.5t Mini Digger</span> and <span class="tagline__truck">7t Tip Truck</span>
    </p>

    <ul class="services services--left text-shadowed">
      <li>Hire</li>
      <li>Full Attachments</li>
      <li>Small Aggregate</li>
      <li class="services__wrap">Deliveries</li>
    </ul>

    <ul class="services services--right text-shadowed">
      <li>Augers</li>
      <li>Trenching</li>
      <li>Site Preparation</li>
    </ul>

    <div class="card__band"></div>
    <p class="contact contact--phone">Phone: 0218365914</p>
    <p class="contact contact--email">rudda.rdl@plinto.co.nz</p>
  </main>
</body>
</html>
```